Harbor Lanterns: Walking Beside Young Ones Through Every Season

This book is about being a good father and how to parent them well so they are fully equipped to launch into the world when they become adults. It is an encouraging and practical guide that acknowledges the difficulties of being a good father and provides strategies for addressing them.

Target Market(s)

My target market is dads, or people that will gift this book to a dad that they know

```html
<!DOCTYPE html>
<html lang="en">
<head>
<meta charset="UTF-8">
<title>Harbor Lanterns — Book Cover</title>
<link rel="stylesheet" href="https://fonts.googleapis.com/css2?family=Barlow:wght@500;600&family=Poppins:wght@500&display=swap">
<style>
  :root {
    --cover-brown: #3d221f;
    --cover-brown-deep: #2a1713;
    --sky-ember: #c9663a;
    --sun-gold: #f7c54a;
    --sun-core: #fff2b8;
    --title-white: #ffffff;
    --tagline-gold: #f4cf66;
  }
  html, body {
    margin: 0;
    padding: 0;
    width: 849px;
    height: 1200px;
    overflow: hidden;
    background: var(--cover-brown);
  }
  .cover {
    position: relative;
    width: 849px;
    height: 1200px;
    overflow: hidden;
    background: var(--cover-brown);
  }
  .cover-scene {
    position: absolute;
    left: 0;
    top: 330px;
    width: 849px;
    height: 870px;
    background:
      radial-gradient(ellipse 150px 110px at 214px 518px, var(--sun-core) 0%, var(--sun-gold) 35%, rgba(247,197,74,0) 100%),
      radial-gradient(ellipse 560px 300px at 260px 560px, rgba(240,160,60,0.95) 0%, rgba(201,102,58,0.6) 45%, rgba(61,34,31,0) 100%),
      linear-gradient(180deg,
        var(--cover-brown) 0%,
        #4e2c24 22%,
        #8a4a30 40%,
        #d48a3c 58%,
        #a45a2a 66%,
        #3a2018 76%,
        var(--cover-brown-deep) 100%);
  }
  .title-block {
    position: absolute;
    left: 0;
    top: 0;
    width: 849px;
    text-align: center;
  }
  .title-kicker {
    position: absolute;
    left: 0;
    top: 104px;
    width: 849px;
    margin: 0;
    font-family: "Barlow", sans-serif;
    font-weight: 600;
    font-size: 54px;
    line-height: 1;
    letter-spacing: 24px;
    text-indent: 24px;
    color: var(--title-white);
  }
  .title-outline {
    position: absolute;
    left: 90px;
    top: 160px;
    width: 670px;
    height: 150px;
  }
  .title-outline text {
    font-family: "Poppins", sans-serif;
    font-weight: 500;
    font-size: 150px;
    fill: none;
    stroke: url(#outlineFade);
    stroke-width: 1.6;
  }
  .tagline {
    position: absolute;
    left: 0;
    top: 316px;
    width: 849px;
    margin: 0;
    font-family: "Barlow", sans-serif;
    font-weight: 500;
    font-size: 17px;
    letter-spacing: 1.6px;
    color: var(--tagline-gold);
    text-align: center;
  }
</style>
</head>
<body>
  <main class="cover">
    <div class="cover-scene" role="img" aria-label="Photograph of a father holding a small child's hand, walking away across a grassy field toward a glowing sunset, silhouetted against an orange sky"></div>

    <header class="title-block">
      <h1 class="title-kicker">HARBOR</h1>
      <svg class="title-outline" viewBox="0 0 670 150" aria-label="Lanterns">
        <defs>
          <linearGradient id="outlineFade" x1="0" y1="0" x2="0" y2="1">
            <stop offset="0%" stop-color="#ffffff"/>
            <stop offset="60%" stop-color="#d8cfcc"/>
            <stop offset="100%" stop-color="#5e4640"/>
          </linearGradient>
        </defs>
        <text x="0" y="136" textLength="666" lengthAdjust="spacingAndGlyphs">Lanterns</text>
      </svg>
      <p class="tagline">WALKING BESIDE YOUNG ONES THROUGH EVERY SEASON</p>
    </header>
  </main>
</body>
</html>
```